Quillory Nest Business Card

I need a business card design. We are a collaborate online training company. Our colors are gray and green. Our website is QuilloryNest.com

I would like an area for a profile picture within the card

```html
<!DOCTYPE html>
<html lang="en">
<head>
<meta charset="UTF-8">
<title>Quillory Nest – Business Card</title>
<link rel="stylesheet" href="https://fonts.googleapis.com/css2?family=Roboto+Condensed:wght@300&display=swap">
<style>
  :root {
    --card-bg: #e6e6e6;
    --panel-gray: #666666;
    --photo-gray: #7a7a7a;
    --accent-green: #99ff00;
    --ink-dark: #111111;
    --ink-light: #f2f2f2;
  }
  * { margin: 0; padding: 0; box-sizing: border-box; }
  html, body {
    width: 1200px;
    height: 667px;
    overflow: hidden;
    background: var(--card-bg);
  }
  .business-card {
    position: relative;
    width: 1200px;
    height: 667px;
    background: var(--card-bg);
    overflow: hidden;
    font-family: "Roboto Condensed", "Arial Narrow", sans-serif;
    font-weight: 300;
  }
  .card-shapes {
    position: absolute;
    inset: 0;
    width: 1200px;
    height: 667px;
  }
  .accent-wave { fill: var(--accent-green); }
  .gray-panel { fill: var(--panel-gray); }
  .profile-photo {
    position: absolute;
    left: 140px;
    top: 110px;
    width: 240px;
    height: 240px;
    border-radius: 50%;
    background: var(--photo-gray);
    border: 6px solid var(--accent-green);
  }
  .website {
    position: absolute;
    left: 592px;
    top: 78px;
    font-size: 61px;
    line-height: 1;
    color: var(--ink-dark);
    letter-spacing: -0.5px;
    white-space: nowrap;
  }
  .contact-list {
    position: absolute;
    left: 45px;
    top: 466px;
    list-style: none;
    color: var(--ink-light);
    font-size: 39px;
    line-height: 51px;
    letter-spacing: -0.4px;
    white-space: nowrap;
  }
  .contact-label {
    display: inline-block;
    width: 113px;
  }
</style>
</head>
<body>
  <main class="business-card">
    <svg class="card-shapes" viewBox="0 0 1063 591" preserveAspectRatio="none" aria-hidden="true">
      <path class="accent-wave" d="M0,0 L322,0 C395,100 500,160 605,210 C715,262 770,305 757,365 C745,425 700,515 662,591 L0,591 Z"/>
      <path class="gray-panel" d="M0,0 L305,0 C375,105 480,165 580,215 C680,262 728,300 718,360 C706,420 662,510 620,591 L0,591 Z"/>
    </svg>

    <div class="profile-photo" role="img" aria-label="Profile photo of the trainer"></div>

    <p class="website">www.quillorynest.com</p>

    <ul class="contact-list">
      <li><span class="contact-label">Phone :</span>000000</li>
      <li><span class="contact-label">Mobile :</span>0000000000</li>
      <li><span class="contact-label">e-mail :</span>hello@quillorynest.com</li>
    </ul>
  </main>
</body>
</html>
```